Flyer Promoting Dental Benefit Program

I want to promote a dental benefit program to my patients that do not have dental insurance. This flyer would be posted in our waiting room and where people make payments. The goal would be to get those interested to request more information and enroll in the program. I have a card that will be issued that has a logo. Theflyer and card should feel congruent. I've uploaded a file with a copy of that card.
The plan costs $290/person. It includes 2 cleanings, exams, and x-rays. It also includes a 20% discount off of our standard fees. The plan or membership lasts for one year. It is only available to those without insurance. It is also important to let people know that this is not insurance (some kind of a disclaimer).
Updates
This plan is only available to patients at my office. The contact information is: Harborview Dental, 2718 West 4600 North Suite 209, Salt Lake City, Utah 84196. (801) 555-0187. info@harborviewdentalexample.com. It is not necessary to include contact information as this flyer will be used as in-office promotion.
Target Market(s)
Those without dental insurance, but have resources to afford dental care.
Industry/Entity Type
Insurance
Look and feel
Each slider illustrates characteristics of the customer's brand and the style your logo design should communicate.

```html
<!DOCTYPE html>
<html lang="en">
<head>
<meta charset="utf-8">
<title>Affordable Dental Plan Flyer</title>
<link rel="stylesheet" href="https://fonts.googleapis.com/css2?family=Arimo:wght@400;700&display=swap">
<style>
  :root {
    --page-bg: #ecece8;
    --paper: #ffffff;
    --green: #a9d46a;
    --green-light: #d6ebb4;
    --green-pale: #eef7e1;
    --green-deep: #6ea83a;
    --tick: #4f9a1e;
    --ink: #151515;
    --ink-soft: #444444;
    --photo-a: #d9d2cc;
    --photo-b: #efe7e4;
  }
  * { box-sizing: border-box; margin: 0; padding: 0; }
  html, body { width: 1200px; height: 900px; overflow: hidden; }
  body {
    background: var(--page-bg);
    font-family: "Arimo", Arial, sans-serif;
    color: var(--ink);
    display: flex; align-items: center; justify-content: center;
  }
  .flyer {
    position: relative;
    width: 620px; height: 860px;
    background: linear-gradient(180deg, var(--paper) 0%, var(--green-pale) 60%, var(--paper) 100%);
    overflow: hidden;
    box-shadow: 0 4px 18px rgba(0,0,0,.15);
  }
  .headline-band {
    height: 72px;
    background: var(--green);
    display: flex; align-items: center; justify-content: center;
  }
  .headline-band h1 {
    font-weight: 400; font-size: 27px; letter-spacing: -0.3px;
  }
  .brand {
    position: absolute; left: 34px; top: 140px;
    display: flex; align-items: center; gap: 10px;
  }
  .brand-dot {
    width: 54px; height: 54px; border-radius: 50%;
    background: var(--green-deep);
  }
  .brand-name {
    font-weight: 700; font-size: 22px; color: var(--ink-soft);
    line-height: 1.05;
  }
  .photo {
    position: absolute; right: 26px; top: 92px;
    width: 290px; height: 150px;
    background: linear-gradient(120deg, var(--photo-a), var(--photo-b));
  }
  .offer {
    position: absolute; top: 262px; left: 0; right: 0; text-align: center;
  }
  .offer h2 { font-size: 25px; font-weight: 700; }
  .offer .price { font-size: 14px; margin-top: 8px; }
  .benefits {
    position: absolute; top: 340px; left: 150px;
    list-style: none;
  }
  .benefits li {
    display: flex; align-items: center; gap: 8px;
    font-size: 17px; margin-bottom: 9px;
  }
  .benefits svg { width: 16px; height: 16px; flex: none; }
  .wave { position: absolute; left: 0; bottom: 0; width: 620px; height: 420px; }
  .disclaimer {
    position: absolute; right: 28px; top: 506px;
    width: 262px; height: 122px;
    border: 3px dashed var(--ink-soft);
    background: var(--paper);
    padding: 10px 12px;
    font-size: 9px; line-height: 1.45; text-align: center;
  }
  .badge {
    position: absolute; left: 30px; bottom: 28px;
    width: 222px; height: 196px;
    background: linear-gradient(160deg, var(--green) 0%, var(--green-light) 100%);
  }
  .cta { position: absolute; left: 264px; top: 674px; }
  .cta .enroll { font-size: 33px; font-weight: 400; letter-spacing: -0.5px; white-space: nowrap; }
  .cta .inquire { font-size: 18px; margin: 8px 0 0 104px; }
</style>
</head>
<body>
  <article class="flyer">
    <header class="headline-band">
      <h1>Do you want a dental benefits that makes sense</h1>
    </header>

    <div class="brand">
      <span class="brand-dot"></span>
      <span class="brand-name">Brightbite<br>Care Plan</span>
    </div>

    <div class="photo" role="img" aria-label="Photo of a smiling senior couple with a handwritten note about discounted fees"></div>

    <section class="offer">
      <h2>Affordable Dental Plan</h2>
      <p class="price">$290/person</p>
    </section>

    <ul class="benefits">
      <li><svg viewBox="0 0 16 16"><path d="M2 8.5l4 4L14 3" fill="none" stroke="var(--tick)" stroke-width="3"/></svg>It includes 2 cleanings, exams, and x-rays</li>
      <li><svg viewBox="0 0 16 16"><path d="M2 8.5l4 4L14 3" fill="none" stroke="var(--tick)" stroke-width="3"/></svg>20% discount off of our standard fees</li>
      <li><svg viewBox="0 0 16 16"><path d="M2 8.5l4 4L14 3" fill="none" stroke="var(--tick)" stroke-width="3"/></svg>Membership fee guaranteed for one year</li>
      <li><svg viewBox="0 0 16 16"><path d="M2 8.5l4 4L14 3" fill="none" stroke="var(--tick)" stroke-width="3"/></svg>Available to those without insurance</li>
    </ul>

    <svg class="wave" viewBox="0 0 620 420" preserveAspectRatio="none" aria-hidden="true">
      <path d="M0 250 C180 250 360 200 470 120 C540 70 590 30 620 10 L620 420 L0 420 Z" fill="var(--green-light)"/>
      <path d="M0 300 C200 290 380 230 500 140 C560 95 600 60 620 45 L620 420 L0 420 Z" fill="var(--green)"/>
    </svg>

    <p class="disclaimer">This is NOT a health insurance plan but a discount benefits program. It does not make payments to any dental or medical providers. The plan does not pay claims or receive premium payments. This program is a fee-for-service plan that gives members access to discounts that they cannot negotiate alone.</p>

    <div class="badge" role="img" aria-label="Green promotional graphic asking whether dental is missing from your benefits package"></div>

    <div class="cta">
      <p class="enroll">Why wait? Enroll now.</p>
      <p class="inquire">Inquire Inside</p>
    </div>
  </article>
</body>
</html>
```